Property Management Company

We are looking for a sharp/modern business card design for a property management company.
We have included what should be on the business card down below in business card details.
Target Market(s)
Commercial properties, Home Owners
Industry/Entity Type
Business
Contact Information for Business Card
Name: Dale Orsino | Owner
Business Name : Kestrel Yards
Slogan : A Smarter Choice
Phone : 555.304.8862
Website: www.kestrelyards.example
E-Mail : dale@kestrelyards.example
Our Services are Commercial & Residential
-Asphalt Maintenance
-Snow Management
-Landscaping
-Blacktop
Free Estimates
Free parking lot cleanup & restripe with snow removal contract
Look and feel

```html
<!DOCTYPE html>
<html lang="en">
<head>
<meta charset="utf-8">
<title>Kestrel Yards – Business Card</title>
<link rel="stylesheet" href="https://fonts.googleapis.com/css2?family=Josefin+Sans:wght@300;400;600;700&display=swap">
<style>
  :root {
    --navy: #13244a;
    --green: #1e8a3e;
    --white: #ffffff;
    --edge: #b9bcc2;
    --page: #ffffff;
  }
  * { box-sizing: border-box; margin: 0; padding: 0; }
  html, body { width: 803px; height: 1200px; overflow: hidden; background: var(--page); }
  body { position: relative; font-family: "Josefin Sans", sans-serif; color: var(--navy); }

  .card {
    position: absolute; left: 145px; width: 501px; height: 287px;
    background: var(--white); border: 1px solid var(--edge); overflow: hidden;
  }
  .card-front { top: 43px; }
  .card-back { top: 346px; }

  .identity-panel {
    position: absolute; left: 16px; top: 0; width: 308px; height: 267px;
    background: var(--navy); color: var(--white);
  }
  .person-name { position: absolute; left: 18px; top: 60px; font-size: 22px; font-weight: 300; letter-spacing: 0.5px; }
  .person-role { position: absolute; left: 19px; top: 86px; font-size: 8px; font-weight: 300; letter-spacing: 6px; }

  .contact-list { position: absolute; left: 19px; top: 171px; list-style: none; }
  .contact-list li { display: flex; align-items: center; height: 19px; font-size: 11px; font-weight: 300; }
  .contact-list svg { width: 12px; height: 12px; margin-right: 12px; flex: none; }

  .brand-name {
    font-family: "Josefin Sans", sans-serif; font-weight: 700; color: var(--navy);
    text-align: center; line-height: 1; position: absolute;
  }
  .card-front .brand-name { left: 324px; width: 177px; top: 112px; font-size: 19px; }
  .card-back .brand-name { left: 0; width: 501px; top: 112px; font-size: 30px; }

  .slogan { position: absolute; text-align: center; font-weight: 300; letter-spacing: 2.5px; color: var(--navy); }
  .card-front .slogan { left: 324px; width: 177px; top: 182px; font-size: 9.5px; }
  .card-back .slogan { left: 0; width: 501px; top: 204px; font-size: 14px; letter-spacing: 3.5px; }

  .services { position: absolute; left: 0; width: 501px; font-size: 5.6px; white-space: nowrap; padding-left: 20px; }
  .services strong { font-weight: 400; font-size: 6.4px; margin-right: 6px; }
  .card-front .services { top: 272px; color: var(--navy); }
  .card-back .services {
    top: 224px; height: 22px; line-height: 23px; background: var(--navy); color: var(--white);
  }
</style>
</head>
<body>

<section class="card card-front" aria-label="Card front">
  <div class="identity-panel">
    <p class="person-name">DALE ORSINO</p>
    <p class="person-role">OWNER</p>
    <ul class="contact-list">
      <li>
        <svg viewBox="0 0 12 12"><rect width="12" height="12" rx="2" fill="#fff"/><path d="M3.5 2.8c.4-.3.9-.2 1.1.2l.6 1.1c.2.4 0 .7-.3.9l-.4.3c.3.9 1 1.6 1.9 2l.3-.4c.2-.3.6-.4.9-.2l1.1.6c.4.2.5.7.2 1.1-.6.8-1.5 1-2.4.6C4.8 8.3 3.5 7 2.8 5.2c-.3-.9 0-1.8.7-2.4z" fill="#13244a"/></svg>
        555.304.8862
      </li>
      <li>
        <svg viewBox="0 0 12 12"><rect width="12" height="12" rx="2" fill="#fff"/><rect x="2.2" y="3.5" width="7.6" height="5.4" fill="none" stroke="#13244a" stroke-width="1"/><path d="M2.2 3.5L6 6.6l3.8-3.1" fill="none" stroke="#13244a" stroke-width="1"/></svg>
        dale@kestrelyards.example
      </li>
      <li>
        <svg viewBox="0 0 12 12"><circle cx="6" cy="6" r="6" fill="#fff"/><text x="6" y="7.4" font-size="3.6" text-anchor="middle" fill="#13244a" font-family="sans-serif" font-weight="700">www</text></svg>
        www.kestrelyards.example
      </li>
    </ul>
  </div>
  <p class="brand-name">KESTREL<br>YARDS</p>
  <p class="slogan">" A SMARTER CHOICE "</p>
  <p class="services"><strong>COMMERCIAL &amp; RESIDENTIAL :</strong>* Asphalt Maintenance* Snow Management* Landscaping* Blacktop Free Estimates* Free parking lot cleanup* Restripe with snow removal contract</p>
</section>

<section class="card card-back" aria-label="Card back">
  <p class="brand-name">KESTREL<br>YARDS</p>
  <p class="slogan">" A SMARTER CHOICE "</p>
  <p class="services"><strong>COMMERCIAL &amp; RESIDENTIAL :</strong>* Asphalt Maintenance* Snow Management* Landscaping* Blacktop Free Estimates* Free parking lot cleanup* Restripe with snow removal contract</p>
</section>

</body>
</html>
```